HR consultancy website - Wordpress Design Project

We need a wordpress design for a new company based in Belgium called Brivolane. We propose HR consultancy services focused on employees' engagement (motivation). We target corporations from 100 to 1000+ employees mainly in Europe.
We need a new design for our existing website (www.brivolane.eu).
We find the current design too static and outdated and we are looking for a more appealing look & feel.
Nevertheless, it has also to be sober.
The colours of the logo (dark blue, purple and light grey) should be preferrably used.
The content structure and the texts remain the same.

Target Market(s)

HR managers, general managers of SME's, higher education

Industry/Entity Type

It Company

Requirements
Must have
• No specific functionalities, except a contact form.

```html
<!DOCTYPE html>
<html lang="en">
<head>
<meta charset="utf-8">
<title>Brivolane – HR engagement consultancy</title>
<link rel="stylesheet" href="https://fonts.googleapis.com/css2?family=PT+Sans:wght@400;700&family=Questrial&display=swap">
<style>
  :root {
    --header-dark: #333333;
    --header-edge: #dedede;
    --nav-active: #0e96b0;
    --white: #ffffff;
    --ink: #333333;
    --rule: #b3b3b3;
    --green: #5ab90c;
    --green-deep: #3f8d05;
    --blue: #72c1d3;
    --pink: #e9629f;
    --orange: #f4b864;
    --footer-line: #e3e3e3;
    --copyright: #6aaee0;
  }
  * { box-sizing: border-box; margin: 0; padding: 0; }
  html, body { width: 1200px; height: 729px; overflow: hidden; background: var(--white); }
  body { position: relative; font-family: "PT Sans", sans-serif; color: var(--ink); }

  .site-header {
    position: absolute; top: 0; left: 0; width: 1200px; height: 92px;
    background: var(--header-dark);
    border-bottom: 8px solid var(--header-edge);
  }
  .brand {
    position: absolute; left: 165px; top: 18px;
    display: flex; align-items: center; gap: 12px;
    font-family: "Questrial", sans-serif; font-size: 40px; color: #d9d9d9;
    letter-spacing: 1px;
  }
  .brand-dot { width: 14px; height: 14px; border-radius: 50%; background: #d9d9d9; }
  .main-nav { position: absolute; right: 140px; top: 26px; display: flex; gap: 6px; }
  .main-nav a {
    display: block; padding: 4px 14px 6px; border-radius: 4px;
    color: var(--white); text-decoration: none; font-weight: 700; font-size: 17px;
  }
  .main-nav a.is-active { background: var(--nav-active); }

  .services { position: absolute; top: 166px; left: 0; width: 1200px; }
  .service { position: absolute; width: 200px; text-align: center; }
  .service-ring { display: block; margin: 0 auto; }
  .service-title {
    margin: 26px auto 0; width: 166px;
    font-family: "Questrial", sans-serif; font-weight: 400; font-size: 28px;
    letter-spacing: 1px; padding-bottom: 2px; border-bottom: 2px solid var(--rule);
  }
  .service-link { display: block; margin-top: 5px; font-size: 16px; text-decoration: none; }
  .service--evaluation { left: 164px; }
  .service--strategy { left: 390px; }
  .service--process { left: 621px; }
  .service--impact { left: 846px; }
  .service--evaluation .service-link { color: var(--green); }
  .service--strategy .service-link { color: var(--blue); }
  .service--process .service-link { color: var(--pink); }
  .service--impact .service-link { color: var(--orange); }

  .intro-panel {
    position: absolute; left: 176px; top: 477px; width: 851px; height: 124px;
    background: linear-gradient(180deg, #66c215 0%, var(--green) 70%, var(--green-deep) 100%);
    border-bottom: 6px solid var(--green-deep);
    color: var(--white); font-size: 19.5px; line-height: 25px;
    padding: 37px 30px 0 35px;
  }
  .intro-pointer {
    position: absolute; left: 244px; top: 457px;
    width: 0; height: 0;
    border-left: 12px solid transparent; border-right: 12px solid transparent;
    border-bottom: 21px solid var(--green);
  }

  .site-footer {
    position: absolute; left: 0; top: 671px; width: 1200px; height: 58px;
    border-top: 1px solid var(--footer-line); text-align: center;
  }
  .footer-nav { margin-top: 13px; font-size: 12px; color: var(--ink); }
  .footer-nav a { color: var(--ink); text-decoration: none; }
  .footer-nav .sep { margin: 0 5px; }
  .copyright { margin-top: 5px; font-size: 12px; color: var(--copyright); }
</style>
</head>
<body>

<header class="site-header">
  <div class="brand"><span class="brand-name">BRIVOLANE</span><span class="brand-dot"></span></div>
  <nav class="main-nav">
    <a href="#" class="is-active">home</a>
    <a href="#">register</a>
    <a href="#">login</a>
    <a href="#">contact</a>
  </nav>
</header>

<main>
  <section class="services">
    <article class="service service--evaluation">
      <svg class="service-ring" width="190" height="190" viewBox="0 0 190 190" aria-hidden="true">
        <circle cx="95" cy="95" r="89" fill="none" stroke="var(--green)" stroke-width="10"/>
        <g fill="none" stroke="var(--green)" stroke-width="4">
          <circle cx="82" cy="91" r="33"/>
          <ellipse cx="82" cy="91" rx="14" ry="33"/>
          <line x1="49" y1="91" x2="115" y2="91"/>
          <line x1="53" y1="74" x2="111" y2="74"/>
          <line x1="53" y1="108" x2="111" y2="108"/>
          <line x1="82" y1="58" x2="82" y2="124"/>
        </g>
        <circle cx="104" cy="87" r="17" fill="var(--white)" stroke="var(--green)" stroke-width="5"/>
        <line x1="117" y1="100" x2="138" y2="116" stroke="var(--green)" stroke-width="9" stroke-linecap="round"/>
      </svg>
      <h2 class="service-title">EVALUATION</h2>
      <a class="service-link" href="#">View More</a>
    </article>

    <article class="service service--strategy">
      <svg class="service-ring" width="190" height="190" viewBox="0 0 190 190" aria-hidden="true">
        <circle cx="95" cy="95" r="89" fill="none" stroke="var(--blue)" stroke-width="10"/>
        <g stroke="var(--blue)" stroke-width="4" stroke-linecap="round">
          <line x1="50" y1="55" x2="50" y2="135"/>
          <line x1="72" y1="55" x2="72" y2="135"/>
          <line x1="94" y1="55" x2="94" y2="135"/>
          <line x1="116" y1="55" x2="116" y2="135"/>
          <line x1="138" y1="55" x2="138" y2="135"/>
        </g>
        <g fill="var(--blue)">
          <circle cx="50" cy="109" r="7"/>
          <circle cx="72" cy="92" r="7"/>
          <circle cx="94" cy="113" r="7"/>
          <circle cx="116" cy="85" r="7"/>
          <circle cx="138" cy="97" r="7"/>
        </g>
      </svg>
      <h2 class="service-title">STRATEGY</h2>
      <a class="service-link" href="#">View More</a>
    </article>

    <article class="service service--process">
      <svg class="service-ring" width="190" height="190" viewBox="0 0 190 190" aria-hidden="true">
        <circle cx="95" cy="95" r="89" fill="none" stroke="var(--pink)" stroke-width="10"/>
        <circle cx="95" cy="95" r="49" fill="none" stroke="var(--pink)" stroke-width="6"/>
        <polyline points="95,54 95,102 74,122" fill="none" stroke="var(--pink)" stroke-width="6" stroke-linecap="round" stroke-linejoin="round"/>
      </svg>
      <h2 class="service-title">PROCESS</h2>
      <a class="service-link" href="#">View More</a>
    </article>

    <article class="service service--impact">
      <svg class="service-ring" width="190" height="190" viewBox="0 0 190 190" aria-hidden="true">
        <circle cx="95" cy="95" r="89" fill="none" stroke="var(--orange)" stroke-width="10"/>
        <circle cx="95" cy="95" r="24" fill="none" stroke="var(--orange)" stroke-width="48" stroke-dasharray="2.2 2.16"/>
        <circle cx="95" cy="95" r="48" fill="none" stroke="var(--orange)" stroke-width="2.5"/>
      </svg>
      <h2 class="service-title">IMPACT</h2>
      <a class="service-link" href="#">View More</a>
    </article>
  </section>

  <span class="intro-pointer" aria-hidden="true"></span>
  <section class="intro-panel">
    <p>Our ERM tool creates an HR engagement cycle to encourage line managers to take initiatives and to enhance the engagement of their team members.</p>
  </section>
</main>

<footer class="site-footer">
  <nav class="footer-nav">
    <a href="#">about us</a><span class="sep">|</span><a href="#">services</a><span class="sep">|</span><a href="#">support</a><span class="sep">|</span><a href="#">testimonials</a><span class="sep">|</span><a href="#">reports</a><span class="sep">|</span><a href="#">future</a><span class="sep">|</span><a href="#">latest</a><span class="sep">|</span><a href="#">meetings</a><span class="sep">|</span><a href="#">contact us</a>
  </nav>
  <p class="copyright">Copyright ©&nbsp; brivolane &amp; Co All Rights Reserved</p>
</footer>

</body>
</html>
```